Letterhead - Pelvarosi Law Group

I receive a fantastic logo from you guys and I'd like to incorporate it into business cards and letterhead. I accidentally approved design No. 58027913 and contacted designer Tarveck, and Tarveck sent me the zip folder for Design No. 58027986, which I very much appreciate.
I'd like to order business cards and letterhead with Design No. 58027986 as soon as possible, but I want to make sure that you incorporate the correct design (attached). I'd also like to provide my information to add (address, phone number, email, fax) but I'm not quite sure how to do it.
The information that I would like on the business cards and letterhead is as follows:
Pelvarosi Law Group
Dorian K. Pelvarosi, Esq.
2741 Halvern Street, Suite 306
San Francisco, CA 94019
Office: (415) 738-0461
Fax: (415) 386-7710
dory@pelvarosilawgroup.com
Thanks in advance for any guidance.
Dory Pelvarosi
Pelvarosi Law Group
(415) 574-8839 (cell)

```html
<!DOCTYPE html>
<html lang="en">
<head>
<meta charset="utf-8">
<title>Pelvarosi Law Group – Stationery</title>
<link rel="stylesheet" href="https://fonts.googleapis.com/css2?family=Montserrat:wght@400;500;700&family=Lato:wght@400;700&family=Great+Vibes&display=swap">
<style>
  :root{
    --backdrop:#e6e6e6;
    --paper:#ffffff;
    --ink:#1d1d1b;
    --brand-blue:#0a8ec8;
    --card-dark:#1d1d1b;
    --on-dark:#ffffff;
  }
  *{margin:0;padding:0;box-sizing:border-box}
  html,body{width:1200px;height:933px;overflow:hidden;background:var(--backdrop)}
  .canvas{position:relative;width:1200px;height:933px}

  /* Letterhead */
  .letterhead{position:absolute;left:98px;top:53px;width:550px;height:777px;background:var(--paper);overflow:hidden;color:var(--ink)}
  .brand-name{font-family:'Montserrat',sans-serif;font-weight:700;letter-spacing:.04em;text-transform:uppercase;line-height:1.1}
  .letterhead .brand-name{position:absolute;left:28px;top:90px;width:150px;font-size:15px;color:var(--ink)}
  .letterhead .brand-name::before{content:"";display:block;width:12px;height:12px;background:var(--brand-blue);margin-bottom:8px}
  .lh-address{position:absolute;right:208px;top:40px;text-align:right;font-family:'Montserrat',sans-serif;font-size:9.3px;line-height:11.5px}
  .lh-divider{position:absolute;left:354px;top:42px;width:1px;height:43px;background:var(--brand-blue)}
  .contact-list{list-style:none;font-family:'Montserrat',sans-serif}
  .contact-list li{display:flex;align-items:center;gap:4px}
  .contact-list svg{flex:none;fill:var(--brand-blue)}
  .lh-contacts{position:absolute;left:369px;top:40px;font-size:9.3px;line-height:11.5px}
  .letter{position:absolute;left:28px;top:177px;width:494px;font-family:'Lato',sans-serif;font-size:11px;line-height:12px}
  .letter p{margin-bottom:12px;text-align:justify}
  .letter .date,.letter .recipient{text-align:left}
  .letter .date{font-size:11.5px;margin-bottom:14px}
  .letter .recipient{margin-bottom:12px}
  .letter .salutation{font-weight:700;font-size:13px;margin:16px 0 16px}
  .letter .closing{margin-top:24px;text-align:left}
  .letter .signature{font-family:'Great Vibes',cursive;font-size:24px;margin-top:52px;text-align:left}
  .swoosh{position:absolute;left:0;bottom:0;display:block}

  /* Business cards */
  .card{position:absolute;left:756px;width:345px;height:196px;overflow:hidden}
  .card-front{top:380px;background:var(--card-dark);color:var(--on-dark)}
  .card-front .brand-name{position:absolute;left:25px;top:78px;width:150px;font-size:13px;color:var(--on-dark)}
  .card-front .brand-name::before{content:"";display:block;width:10px;height:10px;background:var(--brand-blue);margin-bottom:7px}
  .card-divider{position:absolute;left:185px;top:46px;width:1px;height:104px;background:var(--brand-blue)}
  .card-details{position:absolute;left:198px;top:44px;font-family:'Montserrat',sans-serif}
  .holder-name{font-weight:700;font-size:12px;color:var(--brand-blue);line-height:13px}
  .holder-title{font-size:7.6px;line-height:10px;margin-bottom:5px}
  .card-address{font-size:7.6px;line-height:9px;margin-bottom:6px}
  .card-details .contact-list{font-size:7.6px;line-height:9px}
  .card-back{top:601px;background:var(--brand-blue);display:flex;align-items:center;justify-content:center}
  .card-back .brand-name{font-size:22px;color:var(--on-dark);text-align:center;letter-spacing:.06em;line-height:1.3}
</style>
</head>
<body>
<div class="canvas">

  <article class="letterhead">
    <div class="brand-name">Pelvarosi Law Group</div>

    <address class="lh-address" style="font-style:normal">
      Pelvarosi Law Group<br>
      Dorian K. Pelvarosi, Esq.<br>
      2741 Halvern Street, Suite 306<br>
      San Francisco, CA 94019
    </address>
    <div class="lh-divider"></div>
    <ul class="contact-list lh-contacts">
      <li><svg width="8" height="7" viewBox="0 0 8 7"><path d="M0 2C2-0.5 6-0.5 8 2L7 3 5.5 2 5.5 1.2C4.5 0.9 3.5 0.9 2.5 1.2L2.5 2 1 3ZM1.5 7 2.5 3H5.5L6.5 7Z"/></svg>(415) 738-0461</li>
      <li><svg width="8" height="8" viewBox="0 0 8 8"><path d="M1 3H7V8H1ZM2 0H6V2.5H2Z"/></svg>(415) 386-7710</li>
      <li><svg width="8" height="8" viewBox="0 0 8 8"><path d="M2 0H6V8H2ZM2.8 1V6.5H5.2V1Z"/></svg>(415) 574-8839</li>
      <li><svg width="8" height="6" viewBox="0 0 8 6"><path d="M0 0H8L4 3ZM0 1.2 4 4 8 1.2V6H0Z"/></svg>dory@pelvarosilawgroup.com</li>
    </ul>

    <div class="letter">
      <p class="date">January-03-2020</p>
      <p class="recipient">Mr, Aldo Mercer<br>President</p>
      <p class="recipient">Brevant Corporation<br>123 Street Name, Suite# 10<br>City, State, 120023</p>
      <p class="salutation">Dear Mr, Aldo</p>
      <p>Lorem ipsum dolor sit amet, consectetur adipiscing elit, sed do eiusmod tempor incididunt ut labore et dolore magna aliqua. Ut enim ad minim veniam, quis nostrud exercitation ullamco laboris nisi ut aliquip ex ea commodo consequat. Duis aute irure dolor in reprehenderit in voluptate velit esse cillum dolore eu fugiat nulla pariatur.</p>
      <p>Lorem ipsum dolor sit amet, consectetur adipiscing elit, sed do eiusmod tempor incididunt ut labore et dolore magna aliqua. Ut enim ad minim veniam, quis nostrud exercitation ullamco laboris nisi ut aliquip ex ea commodo consequat. Duis aute irure dolor in reprehenderit in voluptate velit esse cillum dolore eu fugiat nulla pariatur.</p>
      <p>Lorem ipsum dolor sit amet, consectetur adipiscing elit, sed do eiusmod tempor incididunt ut labore et dolore magna aliqua. Ut enim ad minim veniam, quis nostrud exercitation ullamco laboris nisi ut aliquip ex ea commodo consequat.</p>
      <p>Excepteur sint occaecat cupidatat non proident, sunt in culpa qui officia deserunt mollit anim id est laborum. re et dolore magnam aliquam quaerat voluptatem.</p>
      <p class="closing">Regards</p>
      <p class="signature">Lena Ortiz</p>
    </div>

    <svg class="swoosh" width="550" height="46" viewBox="0 0 550 46">
      <path d="M15 46Q275 -46 535 46Q275 -26 15 46Z" fill="var(--ink)"/>
      <path d="M17 46Q275 -18 531 46Z" fill="var(--brand-blue)"/>
    </svg>
  </article>

  <section class="card card-front">
    <div class="brand-name">Pelvarosi Law Group</div>
    <div class="card-divider"></div>
    <div class="card-details">
      <p class="holder-name">CORWIN ADLEY</p>
      <p class="holder-title">General Manager</p>
      <p class="card-address">Pelvarosi Law Group<br>Dorian K. Pelvarosi, Esq.<br>2741 Halvern Street, Suite 306<br>San Francisco, CA 94019</p>
      <ul class="contact-list">
        <li><svg width="6" height="5" viewBox="0 0 8 7"><path d="M0 2C2-0.5 6-0.5 8 2L7 3 5.5 2 5.5 1.2C4.5 0.9 3.5 0.9 2.5 1.2L2.5 2 1 3ZM1.5 7 2.5 3H5.5L6.5 7Z"/></svg>(415) 738-0461</li>
        <li><svg width="6" height="6" viewBox="0 0 8 8"><path d="M1 3H7V8H1ZM2 0H6V2.5H2Z"/></svg>(415) 386-7710</li>
        <li><svg width="6" height="6" viewBox="0 0 8 8"><path d="M2 0H6V8H2ZM2.8 1V6.5H5.2V1Z" fill="var(--on-dark)"/></svg>(415) 574-8839</li>
        <li><svg width="6" height="5" viewBox="0 0 8 6"><path d="M0 0H8L4 3ZM0 1.2 4 4 8 1.2V6H0Z"/></svg>dory@pelvarosilawgroup.com</li>
      </ul>
    </div>
    <svg class="swoosh" width="345" height="30" viewBox="0 0 345 30">
      <path d="M10 30Q172 -30 335 30Q172 -16 10 30Z" fill="var(--on-dark)"/>
      <path d="M12 30Q172 -12 333 30Z" fill="var(--brand-blue)"/>
    </svg>
  </section>

  <section class="card card-back">
    <div class="brand-name">Pelvarosi<br>Law Group</div>
  </section>

</div>
</body>
</html>
```